Brisk Lyceum Website

We are looking for a new design of our website. The current website is www.brisklyceum-example.com. The company is the #1 pre-college math and science program in Orange County, CA. We would like to see designs that integrate our logo with a modern color scheme. We are also open for suggestions that could improve our logo. We would like a simple, minimal, clean, classy, and vibrant front-page user interface design that give the premium, modern, innovative, creative, and premier brand feel. We like the "New Retro Colors for the Web" as described here: http://www.pixelharbor-example.net/en/layout-notes-2013/.

Target Market(s)

The target market is parents with K-12 students from a diverse population. Parents are well educated with family income > $150,000. Most of the decision makers are mothers from immigrate families: 30% Chinese, 30% Korean, 15% Indian, 24% White.

Industry/Entity Type

College

Requirements
Must have
• Must read our statement of differentiation at:
• http://brisklyceum-example.com/about-us
• Your design must be reflective of your understanding of the statements.
Nice to have
• The design should also be mobil friendly.
Should not have
• While most of our current classes are math, our company is expanding to include STEM (Science, Technology, Engineering, and Math) for gifted students. Therefore, the site should not be JUST a math education site.

```html
<!DOCTYPE html>
<html lang="en">
<head>
<meta charset="utf-8">
<title>Brisk Lyceum for Gifted Youth</title>
<link rel="stylesheet" href="https://fonts.googleapis.com/css2?family=Open+Sans:wght@400;600;700&display=swap">
<style>
  :root {
    --bg-top: #2c2c2c;
    --bg-mid: #434343;
    --bg-bottom: #282828;
    --white: #ffffff;
    --ink: #111111;
    --navy: #1f2a7a;
    --tab-fill: #e4d8c8;
    --tab-bar: #c9bba8;
    --events: #c9a06e;
    --calendar: #f26b66;
    --news: #79b8a6;
    --dashboard: #5e5a56;
    --scheduler: #9b97c3;
    --about: #777777;
    --locations: #78b8e6;
    --contact: #a19ba3;
    --footer-text: #e6e6e6;
  }
  * { box-sizing: border-box; margin: 0; padding: 0; }
  html, body { width: 881px; height: 1200px; overflow: hidden; }
  body {
    font-family: "Open Sans", sans-serif;
    background: linear-gradient(180deg, var(--bg-top) 0%, var(--bg-mid) 45%, var(--bg-bottom) 100%);
    position: relative;
  }
  .search {
    position: absolute; left: 505px; top: 26px; width: 246px; height: 23px;
    background: linear-gradient(90deg, #d9d9d9, #ffffff 30%);
    border-radius: 12px; border: 1px solid #999;
  }
  .search-label {
    position: absolute; right: 6px; top: 1px; font-size: 17px; color: var(--ink);
    border-left: 1px solid var(--ink); padding-left: 2px; line-height: 20px;
  }
  .login {
    position: absolute; left: 769px; top: 26px; width: 69px; height: 23px;
    background: var(--white); border-radius: 12px; border: 1px solid #999;
    font-size: 17px; line-height: 21px; text-align: center; color: var(--ink);
  }
  .hero {
    position: absolute; left: 40px; top: 65px; width: 800px; height: 451px; overflow: hidden;
  }
  .hero-photo {
    position: absolute; inset: 0;
    background:
      radial-gradient(ellipse 55% 45% at 35% 62%, #e8d2b0 0%, #c9a47a 45%, transparent 75%),
      linear-gradient(180deg, #8a7d6c 0%, #b4a08a 30%, #8f7a5f 60%, #5e4a34 100%);
  }
  .hero-title {
    position: absolute; right: 0; top: 237px; font-size: 72px; font-weight: 400;
    color: var(--white); line-height: 1; letter-spacing: 1px;
  }
  .hero-subtitle {
    position: absolute; right: 38px; top: 324px; font-size: 50px; font-weight: 400;
    color: var(--white); line-height: 1;
  }
  .subject-tabs {
    position: absolute; left: 0; right: 0; top: 403px; height: 48px;
    background: linear-gradient(180deg, rgba(214,200,182,.75), var(--tab-bar));
    border-radius: 20px 20px 0 0;
    display: flex; align-items: flex-start; padding: 14px 0 0 7px; gap: 6px;
  }
  .subject-tab {
    height: 27px; padding: 0 14px; border-radius: 14px;
    background: var(--tab-fill); font-size: 17px; font-weight: 600;
    color: var(--ink); line-height: 27px; white-space: nowrap;
  }
  .tile {
    position: absolute; width: 240px; height: 88px;
    color: var(--white); font-size: 40px; line-height: 88px; text-align: center;
  }
  .tile.events { left: 38px; top: 552px; background: var(--events); }
  .tile.calendar { left: 314px; top: 552px; background: var(--calendar); }
  .tile.news { left: 587px; top: 552px; background: var(--news); }
  .tile.dashboard { left: 38px; top: 674px; background: var(--dashboard); }
  .tile.scheduler { left: 314px; top: 674px; background: var(--scheduler); }
  .tile.about { left: 587px; top: 674px; background: var(--about); }
  .tile.locations { left: 38px; top: 791px; background: var(--locations); }
  .tile.contact { left: 314px; top: 791px; background: var(--contact); }
  .footer-brand {
    position: absolute; left: 37px; top: 1103px; width: 300px; height: 69px;
    background: var(--white); display: flex; align-items: center; justify-content: center; gap: 10px;
  }
  .footer-brand-mark { width: 22px; height: 22px; background: var(--navy); }
  .footer-brand-name { font-size: 27px; font-weight: 600; color: var(--navy); }
  .footer-info {
    position: absolute; left: 366px; top: 1124px; font-size: 13px; line-height: 22px;
    color: var(--footer-text);
  }
</style>
</head>
<body>
  <div class="search"><span class="search-label">Search</span></div>
  <div class="login">Login</div>

  <header class="hero">
    <div class="hero-photo" role="img" aria-label="Open book in front of a blurred shelf of colourful books"></div>
    <div class="hero-title">Brisk Lyceum</div>
    <div class="hero-subtitle">for gifted youth</div>
    <nav class="subject-tabs">
      <span class="subject-tab">Maths</span>
      <span class="subject-tab">Physics</span>
      <span class="subject-tab">Chemistry</span>
      <span class="subject-tab">Biology</span>
      <span class="subject-tab">Science Fair</span>
      <span class="subject-tab">Fall 2013</span>
      <span class="subject-tab">Results</span>
    </nav>
  </header>

  <main>
    <div class="tile events">Events</div>
    <div class="tile calendar">Calender</div>
    <div class="tile news">News</div>
    <div class="tile dashboard">Dash Board</div>
    <div class="tile scheduler">Sheduler</div>
    <div class="tile about">About Us</div>
    <div class="tile locations">Locations</div>
    <div class="tile contact">Contact</div>
  </main>

  <footer>
    <div class="footer-brand">
      <span class="footer-brand-mark"></span>
      <span class="footer-brand-name">Brisk Lyceum</span>
    </div>
    <p class="footer-info">Copyright © 2000-2013 , Brisk Lyceum for Gifted Youth.<br>2750 Harbor Loop, Suite 140 Irvine CA 92614. (949) 555-0187</p>
  </footer>
</body>
</html>
```